Packaging label for launch of sun dried tomato products.

Established family farm in South Africa growing fruit for the production of dried fruit. We need a packaging label for the launch of our sun dried tomato products ie dried tomatoes in olive oil, dried tomato flakes and tomato powder. Packaging will be a round glass "jam jar" and spice shaker bottle. Due to limited amount of product available we cannot market to the masses, but rather focus on conveying a message of quality and exclusivity.

Target Market(s)

Home chef

Industry/Entity Type

Food

Font styles to use
Serif

Requirements
Nice to have
• Include the farm name in the design. KEVANTO

```html
<!DOCTYPE html>
<html lang="en">
<head>
<meta charset="utf-8">
<title>KEVANTO – Dried Tomatoes in Olive Oil Label</title>
<link href="https://fonts.googleapis.com/css2?family=Bodoni+Moda:wght@400;500&family=Montserrat:wght@400;600;700&display=swap" rel="stylesheet">
<style>
  :root {
    --page: #ffffff;
    --label-black: #231f20;
    --leaf-green: #2e8540;
    --sun-yellow: #f4a81d;
    --tomato-red: #e0281f;
    --tomato-deep: #b8261a;
    --ink-white: #ffffff;
    --ink-grey: #9a9a9a;
    --crate-wood: #c08a4e;
  }
  * { margin: 0; padding: 0; box-sizing: border-box; }
  html, body {
    width: 1200px; height: 848px; overflow: hidden;
    background: var(--page);
  }
  .label {
    position: absolute; left: 186px; top: 252px;
    width: 818px; height: 402px;
    background: var(--label-black);
    overflow: hidden;
    font-family: "Montserrat", sans-serif;
    color: var(--ink-white);
  }
  .label__art { position: absolute; inset: 0; }
  .brand {
    position: absolute; left: 304px; width: 240px; top: 42px;
    text-align: center;
  }
  .brand__name {
    font-family: "Bodoni Moda", serif; font-weight: 400;
    font-size: 34px; letter-spacing: 0.5px; line-height: 1;
    display: inline-flex; align-items: flex-start; gap: 4px;
  }
  .brand__mark {
    width: 17px; height: 17px; border: 1px solid var(--ink-white);
    border-radius: 50%; margin-top: -16px;
  }
  .brand__tagline {
    font-family: "Bodoni Moda", serif; font-size: 9px;
    letter-spacing: 1px; margin-top: 12px;
  }
  .product-name {
    position: absolute; left: 224px; width: 400px; top: 172px;
    text-align: center; font-family: "Bodoni Moda", serif;
    font-size: 24px; line-height: 32px; letter-spacing: 0.5px;
  }
  .product-visual {
    position: absolute; left: 339px; top: 258px; width: 170px; height: 95px;
    border-radius: 4px;
    background: linear-gradient(180deg, var(--tomato-red) 0 30%, var(--crate-wood) 30% 100%);
  }
  .net-weight {
    position: absolute; left: 324px; width: 200px; top: 368px;
    text-align: center; font-family: "Bodoni Moda", serif; font-size: 12px;
  }
  .story {
    position: absolute; left: 42px; top: 199px; width: 190px;
    font-size: 10px; line-height: 12.5px; color: var(--ink-grey);
  }
  .badges {
    position: absolute; left: 58px; top: 275px; display: flex; gap: 20px;
  }
  .badge { width: 52px; text-align: center; }
  .badge__icon {
    width: 31px; height: 31px; margin: 0 auto 6px;
    border: 1.5px solid var(--ink-white); border-radius: 50%;
  }
  .badge__text { font-size: 6.5px; font-weight: 700; letter-spacing: 0.8px; line-height: 8px; }
  .origin {
    position: absolute; left: 39px; top: 346px;
    font-size: 12.5px; letter-spacing: 2.4px; color: var(--ink-grey);
  }
  .nutrition {
    position: absolute; left: 610px; top: 152px; width: 180px; height: 148px;
    border: 2px solid var(--ink-white); border-radius: 14px;
    padding: 10px 13px; font-size: 7px; line-height: 9px;
  }
  .nutrition__title { font-size: 13px; line-height: 14px; font-weight: 400; }
  .nutrition__rule { border-top: 2px solid var(--ink-white); margin: 2px 0; }
  .nutrition__row { display: flex; justify-content: space-between; }
  .nutrition__row--calories { font-size: 8px; align-items: flex-end; }
  .nutrition__row--calories strong { font-size: 14px; font-weight: 400; }
  .nutrition__row--boxed {
    border-top: 1px solid var(--label-black); background: var(--ink-white);
    color: var(--label-black); padding: 0 2px; margin: 0 -2px;
  }
  .nutrition__dv { text-align: right; font-size: 5px; }
  .disposal { position: absolute; left: 742px; top: 340px; display: flex; gap: 8px; }
</style>
</head>
<body>
<section class="label">
  <svg class="label__art" width="818" height="402" viewBox="0 0 818 402">
    <g class="bands-left">
      <path d="M150 62 C220 50 260 40 305 38 L305 62 C260 66 210 76 170 90 Z" fill="var(--tomato-red)"/>
      <path d="M0 108 C90 92 200 40 305 20 L305 46 C210 70 110 130 0 150 Z" fill="var(--sun-yellow)"/>
      <path d="M0 162 C110 140 210 90 305 70 L305 108 C210 122 110 172 0 200 Z" fill="var(--leaf-green)"/>
    </g>
    <g class="bands-right">
      <path d="M560 70 C620 62 700 50 818 0 L818 60 C720 90 640 100 560 110 Z" fill="var(--tomato-red)"/>
      <path d="M600 80 C660 90 700 110 818 90 L818 45 C720 70 660 40 600 40 Z" fill="var(--leaf-green)"/>
      <path d="M539 6 C620 10 700 30 818 70 L818 86 C700 56 620 30 539 22 Z" fill="var(--sun-yellow)"/>
      <path d="M539 24 C620 30 700 50 818 88 L818 130 C760 118 700 110 690 170 C680 150 640 135 600 150 C580 110 560 90 539 80 Z" fill="var(--leaf-green)"/>
      <path d="M604 78 L650 90 L640 120 L606 112 Z" fill="var(--tomato-red)"/>
    </g>
    <path class="brand-plaque" d="M304 0 L539 0 L539 115 C480 110 450 100 424 100 C398 100 360 112 304 115 Z" fill="var(--label-black)"/>
    <path role="img" aria-label="Illustrated sliced tomato" d="M0 0 L172 0 C165 70 120 130 60 130 C30 130 10 120 0 110 Z" fill="var(--tomato-red)"/>
    <path role="img" aria-label="Illustrated sliced tomato" d="M672 402 C680 350 740 313 818 313 L818 402 Z" fill="var(--tomato-deep)"/>
  </svg>

  <div class="brand">
    <div class="brand__name">KEVANTO<span class="brand__mark"></span></div>
    <div class="brand__tagline">NATURAL FLAVOR</div>
  </div>

  <h1 class="product-name">DRIED TOMATOES<br>IN OLIVE OIL</h1>
  <div class="product-visual" role="img" aria-label="Watercolour wooden crate filled with ripe tomatoes"></div>
  <div class="net-weight">400g Net</div>

  <p class="story">Lorem ipsum dolor sit amet, consec tetuer adipiscing elit, sed diam nonum my nibh Lorem ipsum dolor sit amet, consectetuer adipiscing elit, sed diam nonummy nibh euismod tincidunt ut</p>

  <div class="badges">
    <div class="badge"><div class="badge__icon"></div><div class="badge__text">HAND<br>CRAFTED</div></div>
    <div class="badge"><div class="badge__icon"></div><div class="badge__text">LOCAL<br>PRODUCTS</div></div>
  </div>
  <p class="origin">made in &nbsp;South Africa</p>

  <div class="nutrition">
    <div class="nutrition__title">NATRITION FACTS</div>
    <div>Serving size 1 cup (110g)</div>
    <div class="nutrition__rule"></div>
    <div>Amount Per Serving</div>
    <div class="nutrition__row nutrition__row--calories"><span>Calories</span><strong>240</strong></div>
    <div class="nutrition__dv">% Daily Value</div>
    <div class="nutrition__row nutrition__row--boxed"><span>Total Fat 3g</span><span>5%</span></div>
    <div class="nutrition__row nutrition__row--boxed"><span>Saturated Fat 1g</span><span>4%</span></div>
    <div class="nutrition__row nutrition__row--boxed"><span>Trans Fat 0g</span><span></span></div>
    <div class="nutrition__row nutrition__row--boxed"><span>Cholesterol 2mg</span><span>0.2%</span></div>
    <div class="nutrition__row nutrition__row--boxed"><span>Sodium 210mg</span><span>7%</span></div>
    <div class="nutrition__row" style="margin-top:2px"><span>Total Carbehydrate 30g</span></div>
  </div>

  <div class="disposal">
    <svg width="24" height="24" viewBox="0 0 24 24" aria-label="Recyclable">
      <path d="M12 3 L17 11 M17 11 L14 11 M17 11 L18 8 M20 15 L16 21 L8 21 M8 21 L10 19 M8 21 L10 23 M4 15 L8 8 L10 11" fill="none" stroke="var(--ink-white)" stroke-width="2.5" stroke-linecap="round"/>
    </svg>
    <svg width="22" height="24" viewBox="0 0 22 24" aria-label="Dispose in bin">
      <path d="M3 5 H19 M8 5 V2 H14 V5 M5 5 L6 22 H16 L17 5 M9 9 V19 M13 9 V19" fill="none" stroke="var(--ink-white)" stroke-width="2"/>
    </svg>
  </div>
</section>
</body>
</html>
```